Design Project - Finance Website (Only need PSD)

UPDATED PROJECT (Now only PSD needed)
Need a Wordpress design for a company called "Tavernor Brook Finance". The company provides finance for corporate clients, businesses and property developers. The design should be business like with appealing colours that communicate trust. I have uploaded a banner and logo to be incorporated or feel free to design something better if you think you can.
** I now only need the PSD
** I want something that is actually designed rather than from a template.
Thanks
Updates
The website will be used for lead generation so the contact form with adjustable fields in the Wordpress backend should be fairly prominent on the page.
I have uploaded a banner and logo for the site. None of the designs I have seen so far were good enough so the first decent design using the new banner and logo provided will win the job. I do not want just a template that has been cut and paste from somewhere else, I want decent design. If anyone provides a decent design then I will give an extra bonus of $150.
Reason: I have uploaded a banner and logo for the site. None of the designs I have seen so far were good enough so the first decent design using the new banner and logo provided will win the job. I do not want just a template that has been cut and paste from somewhere else, I want decent design. If anyone provides a decent design then I will give an extra bonus of $150.
Thanks
Target Market(s)
Business owners & property developers
Industry/Entity Type
Finance
Requirements
Must have
- Contact form on home page that can be altered through the back end eg. ability to add or remove fields. Widgetised sidebars.
Nice to have
- Widgetised footer.

```html
<!DOCTYPE html>
<html lang="en">
<head>
<meta charset="utf-8">
<title>Tavernor Brook Finance</title>
<link href="https://fonts.googleapis.com/css2?family=Source+Sans+3:wght@400;600;700&display=swap" rel="stylesheet">
<style>
:root{
  --backdrop:#474747;
  --page:#ffffff;
  --ink:#2f3638;
  --text:#2a2a2a;
  --blue-hi:#6cc0ea;
  --blue-lo:#2786bf;
  --panel:#8ec7e6;
  --panel-edge:#a9d6ee;
  --footer-hi:#2c2c2c;
  --footer-lo:#050505;
  --footer-text:#e6e6e6;
  --muted:#bdbdbd;
  --accent-red:#e3553c;
}
*{box-sizing:border-box;margin:0;padding:0}
html,body{width:1029px;height:1200px;overflow:hidden;background:var(--backdrop)}
body{font-family:"Source Sans 3",sans-serif;color:var(--text)}
.stage{position:relative;width:1200px;height:1400px;transform:scale(.8575);transform-origin:0 0;background:var(--backdrop)}
.abs{position:absolute}
.page{left:86px;top:0;width:1026px;height:1183px;background:var(--page)}
.logo{left:138px;top:46px;color:var(--ink);font-weight:700;line-height:1}
.logo .name{font-size:34px;letter-spacing:.5px}
.logo .sub{font-size:20px;letter-spacing:6px;margin-top:12px}
.search{left:688px;top:65px;width:305px;height:46px;border-radius:3px;background:linear-gradient(var(--blue-hi),var(--blue-lo))}
.search .field{position:absolute;left:14px;top:9px;width:244px;height:27px;border-radius:3px;background:linear-gradient(#ffffff,#e4e4e4)}
.search .go{position:absolute;left:265px;top:9px;width:28px;height:28px;border-radius:50%;background:var(--accent-red);border:2px solid #f4b3a6}
.social-top{top:70px;width:36px;height:36px;border-radius:3px;background:linear-gradient(var(--blue-hi),var(--blue-lo));border:2px solid #d9e9f2}
.nav{left:117px;top:148px;width:965px;height:55px;border-radius:10px;border:3px solid #d8ecf7;background:linear-gradient(var(--blue-hi),var(--blue-lo));display:flex;align-items:center;justify-content:center;color:#fff;font-size:21px}
.nav span{padding:0 21px}
.nav i{font-style:normal;opacity:.9}
.banner{left:123px;top:220px;width:956px;height:291px;background:linear-gradient(100deg,#5b5f63 0%,#8d959b 35%,#c6cfd4 55%,#a7adb0 75%,#7d8a7c 100%)}
.points{left:615px;top:328px;width:447px;height:157px;background:rgba(0,0,0,.62);color:#fff;font-size:23px;padding:6px 0 0 22px}
.points div{display:flex;align-items:center;height:48px;gap:8px}
.points b{display:inline-flex;width:24px;height:24px;border-radius:50%;background:#fff;color:#111;font-size:16px;justify-content:center;align-items:center}
.dot{top:473px;width:20px;height:20px;border-radius:50%;background:#a9d8ef}
.welcome{left:122px;top:526px;font-size:23px;color:#333;font-weight:400}
.intro{left:126px;top:564px;width:952px;font-size:11.5px;line-height:24px}
.btn{display:flex;align-items:center;justify-content:center;color:#fff;border-radius:12px;background:linear-gradient(var(--blue-hi),var(--blue-lo));border:2px solid #d6ecf8;box-shadow:0 0 0 1px #9cc9e2}
.col-title{font-size:29px;color:#333;font-weight:400}
.panel{top:808px;height:315px;background:var(--panel);border-radius:8px;border:1px solid var(--panel-edge);box-shadow:0 10px 12px -8px rgba(0,0,0,.35)}
.photo{background:linear-gradient(160deg,#3c5d87,#7fa3c6 55%,#b8c9d6);border:1px solid #5a87b0}
.news-text{font-size:11px;line-height:24px;width:210px}
.small{font-size:11px;line-height:24px}
.form-label{font-size:9px;color:#3c4c55}
.input{background:#fff;border:1px solid #c9dbe5;border-radius:2px;font-size:8px;color:#b9c2c7;padding:2px 6px}
.side-bar{left:1126px;top:560px;width:22px;height:93px;border-radius:4px;background:#8b8b8b;display:flex;flex-direction:column;align-items:center;justify-content:space-around;padding:4px 0}
.side-bar span{width:13px;height:13px;border-radius:2px;background:#e9e9e9}
.footer{left:86px;top:1183px;width:1026px;height:217px;background:linear-gradient(var(--footer-hi),var(--footer-lo))}
.f-head{font-size:17px;color:#fff;font-weight:600}
.f-links{font-size:14px;line-height:18px;color:var(--footer-text);list-style:none}
.f-logo{left:798px;top:1240px;color:#4e4e4e;font-weight:700;line-height:1}
.f-logo .name{font-size:28px;letter-spacing:.5px}
.f-logo .sub{font-size:18px;letter-spacing:5px;margin-top:10px}
.copy{left:773px;top:1326px;font-size:13px;color:var(--muted)}
</style>
</head>
<body>
<div class="stage">
  <div class="abs page"></div>

  <div class="abs logo"><div class="name">TAVERNOR BROOK</div><div class="sub">FINANCE</div></div>

  <div class="abs search">
    <div class="field"><svg width="14" height="14" style="margin:6px 0 0 8px"><circle cx="6" cy="6" r="4" fill="none" stroke="#e3553c" stroke-width="2"/><line x1="9" y1="9" x2="13" y2="13" stroke="#e3553c" stroke-width="2"/></svg></div>
    <div class="go"><svg width="24" height="24"><circle cx="11" cy="11" r="5" fill="none" stroke="#fff" stroke-width="2"/><line x1="15" y1="15" x2="19" y2="19" stroke="#fff" stroke-width="2"/></svg></div>
  </div>
  <div class="abs social-top" style="left:1006px" aria-label="Social link"></div>
  <div class="abs social-top" style="left:1050px" aria-label="Social link"></div>

  <nav class="abs nav">
    <span>Home</span><i>|</i><span>About Us</span><i>|</i><span>Services</span><i>|</i><span>Finance</span><i>|</i><span>Real Estate</span><i>|</i><span>Products</span><i>|</i><span>Contact Us</span>
  </nav>

  <div class="abs banner" role="img" aria-label="City street with modern glass office buildings"></div>
  <div class="abs points">
    <div><b>1</b>Compare several capital provider rates</div>
    <div><b>2</b>Access to real estate and hedge funds</div>
    <div><b>3</b>Optimise your capital returns</div>
  </div>
  <div class="abs dot" style="left:156px;background:#fff"></div>
  <div class="abs dot" style="left:184px"></div>
  <div class="abs dot" style="left:212px"></div>

  <h1 class="abs welcome">WELCOME TO TAVERNOR BROOK FINANCE</h1>
  <p class="abs intro">orem Ipsum is simply dummy text of the printing and typesetting industry. Lorem Ipsum has been the industry's standard dummy text ever since the 1500s, when an unknown printer took a galley of type and scrambled it to make a type specimen book. It has survived not only five centuries, but also the leap into electronic typesetting, remaining essentially unchanged. It was popularised in the 1960s with the release of Marlowe Type sheets containing Lorem Ipsum passages, and more recently with desktop publishing software like Quillset Layout including versions of Lorem Ipsum.is a long established fact that a reader will be distracted by the readable content of a page when looking at its layout. The point of using Lorem Ipsum is that it has a more-or-less normal distribution of letters, as opposed to using 'Content here, content here', making it look like readable English. Many desktop publishing packages and web page editors now use Lorem Ipsum as their default model text, and a search for 'lorem ipsum' will uncover many web sites still in their infancy. Various versions have evolved over the years, sometimes by accident, some-</p>
  <div class="abs btn" style="left:985px;top:717px;width:80px;height:28px;font-size:12px">Read more</div>

  <h2 class="abs col-title" style="left:128px;top:766px">Latest News</h2>
  <h2 class="abs col-title" style="left:482px;top:770px">Case study</h2>
  <h2 class="abs col-title" style="left:833px;top:770px">Contact Form</h2>

  <div class="abs panel" style="left:118px;width:343px"></div>
  <div class="abs photo" style="left:130px;top:828px;width:102px;height:83px" role="img" aria-label="Office tower at dusk"></div>
  <p class="abs news-text" style="left:245px;top:830px">Lorem Ipsum is simply dummy text of the printing and typesetting industry. Lorem Ipsum has been the industry's</p>
  <div class="abs photo" style="left:130px;top:929px;width:102px;height:83px" role="img" aria-label="Modern glass building"></div>
  <p class="abs news-text" style="left:245px;top:932px">Lorem Ipsum is simply dummy text of the printing and typesetting industry. Lorem Ipsum has been the industry's</p>
  <div class="abs photo" style="left:130px;top:1030px;width:102px;height:83px" role="img" aria-label="Corporate office block"></div>
  <p class="abs news-text" style="left:245px;top:1036px">Lorem Ipsum is simply dummy text of the printing and typesetting industry. Lorem Ipsum has been the industry's</p>

  <div class="abs panel" style="left:470px;width:344px"></div>
  <div class="abs photo" style="left:487px;top:829px;width:307px;height:124px" role="img" aria-label="Glass skyscraper reflecting the sky"></div>
  <p class="abs small" style="left:488px;top:969px;width:300px">Lorem Ipsum is simply dummy text of the printing and typesetting industry. Lorem Ipsum has been the industry's standard dummy text ever since the 1500s, when an unknown printer took a galley of type and scrambled it to</p>
  <div class="abs btn" style="left:726px;top:1089px;width:66px;height:23px;font-size:9px">Read more</div>

  <div class="abs panel" style="left:826px;width:255px"></div>
  <p class="abs" style="left:841px;top:819px;font-size:11px;color:#3c4c55">Fill in your details and we'll get back to you...</p>
  <span class="abs form-label" style="left:852px;top:853px">Name*</span>
  <div class="abs input" style="left:852px;top:868px;width:219px;height:17px">Full name</div>
  <span class="abs form-label" style="left:853px;top:899px">Phone</span>
  <div class="abs input" style="left:852px;top:913px;width:219px;height:17px">Phone Number</div>
  <span class="abs form-label" style="left:852px;top:944px">Email*</span>
  <div class="abs input" style="left:852px;top:959px;width:219px;height:17px">Email address</div>
  <span class="abs form-label" style="left:852px;top:989px">Message*</span>
  <div class="abs input" style="left:852px;top:1004px;width:219px;height:74px"></div>
  <div class="abs btn" style="left:999px;top:1089px;width:64px;height:23px;font-size:9px">Submit</div>

  <div class="abs side-bar" aria-label="Social links"><span></span><span></span><span></span><span></span></div>

  <footer class="abs footer"></footer>
  <div class="abs f-head" style="left:130px;top:1210px">Latest News</div>
  <ul class="abs f-links" style="left:133px;top:1248px"><li>Home</li><li>About Us</li><li>Services</li><li>Finance</li><li>Real Estate</li><li>Contact Us</li></ul>
  <div class="abs f-head" style="left:271px;top:1211px">Case Study</div>
  <ul class="abs f-links" style="left:275px;top:1243px"><li>Home</li><li>About Us</li><li>Services</li><li>Finance</li><li>Real Estate</li><li>Contact Us</li></ul>
  <div class="abs f-head" style="left:396px;top:1210px">Contact</div>
  <ul class="abs f-links" style="left:399px;top:1248px"><li>Home</li><li>About Us</li><li>Services</li><li>Finance</li><li>Real Estate</li><li>Contact Us</li></ul>
  <div class="abs f-logo"><div class="name">TAVERNOR BROOK</div><div class="sub">FINANCE</div></div>
  <p class="abs copy">Copyrights © Tavernor Brook All Rights Reserved</p>
</div>
</body>
</html>
```